Dog treat bakery needs updated bag labels

We're a small-batch dog treat bakery and would like to update our front bag labels to 1) differentiate our line of products and 2) to stand out on shelves. We believe all dogs deserve to eat clean, healthy foods. That's why we bake low-calorie, clean treats made with simple, premium ingredients like teff, amaranth, and sorghum flours and 100% blueberry, carrot, and purple sweet potato. All our treats are made gluten free without preservatives, artificial flavors, soy, corn, wheat, or eggs. Clean treats, happy dogs!

see uploaded files

```html
<!DOCTYPE html>
<html lang="en">
<head>
<meta charset="utf-8">
<title>Maple's Morsels – Bag Label</title>
<link rel="stylesheet" href="https://fonts.googleapis.com/css2?family=Luckiest+Guy&family=Poppins:wght@400;600;700&display=swap">
<style>
  :root {
    --backdrop: #c6c2b5;
    --sky-blue: #0a8fd6;
    --sky-pale: #e9f4fb;
    --sky-mid: #9fd0ee;
    --badge-teal: #b5dedd;
    --brand-brown: #5c2a2e;
    --title-yellow: #f7e600;
    --slate-text: #3c4257;
    --treat-green: #3aa53a;
    --grass-light: #8fd14a;
    --grass-dark: #2f8a1f;
    --icon-grey: #6f6f6f;
    --white: #ffffff;
  }
  * { margin: 0; padding: 0; box-sizing: border-box; }
  html, body {
    width: 1200px; height: 880px; overflow: hidden;
    background: var(--backdrop);
  }
  .label {
    position: absolute; left: 50px; top: 75px;
    width: 1100px; height: 730px;
    background: var(--white);
    overflow: hidden;
    box-shadow: 0 2px 8px rgba(0,0,0,.12);
  }
  .label__art { position: absolute; inset: 0; }
  .brand-seal {
    position: absolute; left: 36px; top: 123px;
    width: 376px; height: 376px; border-radius: 50%;
    background: var(--badge-teal);
    box-shadow: 0 10px 18px rgba(0,0,0,.28);
    display: flex; align-items: center; justify-content: center;
  }
  .brand-seal__name {
    font-family: 'Poppins', sans-serif; font-weight: 600;
    font-size: 46px; color: var(--brand-brown);
  }
  .treat-tag {
    position: absolute; left: 604px; top: 95px;
    display: flex; align-items: center; gap: 6px;
  }
  .treat-tag__seal {
    width: 48px; height: 48px; border-radius: 50%;
    background: var(--treat-green); border: 3px solid var(--white);
    position: relative; z-index: 1;
  }
  .treat-tag__band {
    margin-left: -20px; padding: 5px 18px 3px 28px;
    background: var(--treat-green);
    clip-path: polygon(4% 0, 100% 0, 97% 100%, 0 100%);
    font-family: 'Luckiest Guy', 'Arial Black', sans-serif; font-size: 30px; line-height: 1.1;
    color: var(--white); letter-spacing: .5px; white-space: nowrap;
  }
  .product-title {
    position: absolute; left: 430px; right: 10px; top: 180px; height: 86px;
    display: flex; align-items: center; justify-content: center;
    white-space: nowrap;
    font-family: 'Luckiest Guy', 'Arial Black', sans-serif; font-size: 68px; line-height: 1;
    font-weight: 400;
    color: var(--brand-brown);
    -webkit-text-stroke: 5px var(--title-yellow);
    paint-order: stroke fill;
    text-shadow: 2px 3px 0 var(--title-yellow);
  }
  .net-weight {
    position: absolute; left: 506px; width: 514px; top: 282px;
    display: flex; align-items: center; gap: 10px; white-space: nowrap;
    font-family: 'Poppins', sans-serif; font-size: 28px; line-height: 1.2; color: var(--slate-text);
  }
  .net-weight::before, .net-weight::after {
    content: ""; flex: 1; border-top: 1px dotted var(--slate-text);
  }
  .tagline {
    position: absolute; left: 450px; width: 600px; top: 398px;
    text-align: center;
    font-family: 'Poppins', sans-serif; font-weight: 600;
    font-size: 31px; line-height: 1.4; color: var(--brand-brown);
  }
  .free-list {
    position: absolute; left: 454px; top: 528px;
    display: flex; gap: 18px; list-style: none;
  }
  .free-list__item {
    width: 98px; height: 98px; border-radius: 50%;
    background: var(--icon-grey); border: 4px solid var(--white);
    outline: 2px solid var(--icon-grey);
    display: flex; flex-direction: column; align-items: center; justify-content: flex-end;
    padding-bottom: 12px;
    font-family: 'Poppins', sans-serif; font-weight: 600; font-size: 15px;
    line-height: 1.05; letter-spacing: 1px; color: var(--white); text-align: center;
  }
  .free-list__item svg { margin-bottom: 6px; }
  .pup-figure {
    position: absolute; left: 185px; top: 538px; width: 80px; height: 58px;
    background: var(--brand-brown); border-radius: 40% 50% 10% 10%;
  }
  .calorie-tag {
    position: absolute; left: 81px; top: 595px; width: 286px; height: 38px;
    background: var(--brand-brown);
    clip-path: polygon(4% 0, 96% 0, 100% 50%, 96% 100%, 4% 100%, 0 50%);
    display: flex; align-items: center; justify-content: center;
    font-family: 'Poppins', sans-serif; font-weight: 600; font-size: 25px;
    color: var(--white); white-space: nowrap;
  }
  .grass-strip {
    position: absolute; left: 0; right: 0; top: 648px; bottom: 0;
    background: linear-gradient(180deg, var(--grass-light), var(--grass-dark));
  }
</style>
</head>
<body>
  <main class="label">
    <svg class="label__art" width="1100" height="730" viewBox="0 0 1100 730" aria-hidden="true">
      <defs>
        <linearGradient id="skyFade" x1="0" y1="0" x2="0" y2="1">
          <stop offset="0" stop-color="#9fd0ee"/>
          <stop offset="1" stop-color="#e9f4fb"/>
        </linearGradient>
        <pattern id="topScallop" width="24" height="46" patternUnits="userSpaceOnUse">
          <path d="M0 0H24V30Q12 46 0 30Z" fill="#0a8fd6"/>
        </pattern>
        <pattern id="midScallop" width="24" height="20" patternUnits="userSpaceOnUse">
          <path d="M0 0H24V5Q12 20 0 5Z" fill="#ffffff"/>
        </pattern>
      </defs>
      <rect x="0" y="340" width="1100" height="390" fill="url(#skyFade)"/>
      <rect x="0" y="338" width="1100" height="20" fill="url(#midScallop)"/>
      <rect x="0" y="0" width="1100" height="46" fill="url(#topScallop)"/>
    </svg>

    <div class="brand-seal"><span class="brand-seal__name">Goofy Pup</span></div>

    <div class="treat-tag">
      <span class="treat-tag__seal"></span>
      <span class="treat-tag__band">DOG TREATS</span>
    </div>

    <h1 class="product-title">MAPLE'S MORSELS</h1>
    <p class="net-weight">NET WT 4 OZ (113 G)</p>

    <p class="tagline">Made with Ancient Grains and Grass<br>fed beef liver</p>

    <ul class="free-list">
      <li class="free-list__item"><svg width="30" height="22" viewBox="0 0 30 22"><ellipse cx="15" cy="11" rx="11" ry="8" fill="#fff"/></svg>SOY<br>FREE</li>
      <li class="free-list__item"><svg width="30" height="22" viewBox="0 0 30 22"><path d="M15 2V21M15 8l-6-4M15 8l6-4M15 14l-6-4M15 14l6-4" stroke="#fff" stroke-width="3" fill="none"/></svg>WHEAT<br>FREE</li>
      <li class="free-list__item"><svg width="30" height="22" viewBox="0 0 30 22"><ellipse cx="15" cy="11" rx="6" ry="10" fill="#fff"/></svg>CORN<br>FREE</li>
      <li class="free-list__item"><svg width="30" height="22" viewBox="0 0 30 22"><path d="M12 1h6v5l3 4v12H9V10l3-4Z" fill="#fff"/></svg>DAIRY<br>FREE</li>
      <li class="free-list__item"><svg width="30" height="22" viewBox="0 0 30 22"><ellipse cx="15" cy="12" rx="7" ry="10" fill="#fff"/></svg>EGG<br>FREE</li>
    </ul>

    <div class="pup-figure" role="img" aria-label="Small brown silhouette of a playful dog bowing"></div>
    <div class="calorie-tag">10 CALORIES EACH</div>

    <div class="grass-strip" role="img" aria-label="Strip of green grass along the bottom edge"></div>
  </main>
</body>
</html>
```